" A Virtal Soluçoes Ambientais é uma empresa que presta serviços de regularizaçao ambiental. Trata-se de uma consultoria ambiental cujo principal serviço é oferecer soluçoes ambientais para atividades produtivas e imóveis urbanos ou rurais. Exemplos: (i) correçao de matrículas e registros em órgao públicos para fazendas produtivas; (ii) correçao de emissoes atmosféricas, ruídos, resíduos, etc, de indústrias; (iii) descontaminaçao do solo ou água subterrânea de um imóvel; (iv) elaboraçao de laudos técnicos sobre passivos ambientais. Observaçao importante: a empresa nao é uma ONG, embora o apelo seja ambiental. "

```html
<!DOCTYPE html>
<html lang="pt-BR">
<head>
<meta charset="utf-8">
<title>Virtal Soluçoes Ambientais – Papel Timbrado</title>
<link href="https://fonts.googleapis.com/css2?family=Questrial&display=swap" rel="stylesheet">
<style>
  :root {
    --backdrop: #e6e6e4;
    --paper: #ffffff;
    --brand-ink: #2f4747;
    --text-ink: #4a5252;
    --band-dark: #2c4338;
    --band-light: #b9c0bc;
  }
  * { box-sizing: border-box; margin: 0; padding: 0; }
  html, body {
    width: 1200px;
    height: 1200px;
    overflow: hidden;
    background: var(--backdrop);
    font-family: "Questrial", "Helvetica Neue", Arial, sans-serif;
  }
  .letterhead {
    position: absolute;
    left: 211px;
    top: 50px;
    width: 778px;
    height: 1100px;
    background: var(--paper);
    box-shadow: 0 2px 10px rgba(0,0,0,0.12);
  }
  .brand-name {
    position: absolute;
    top: 56px;
    left: 0;
    right: 0;
    text-align: center;
    font-size: 52px;
    line-height: 1;
    font-weight: 400;
    color: var(--brand-ink);
  }
  .contact {
    position: absolute;
    left: 14px;
    bottom: 42px;
    font-size: 15px;
    font-style: normal;
    line-height: 1.4;
    color: var(--text-ink);
  }
  .contact .phone { margin-top: 10px; }
  .footer-band {
    position: absolute;
    left: 0;
    right: 0;
    bottom: 0;
    height: 22px;
    background: var(--band-light);
  }
  .footer-band::before {
    content: "";
    position: absolute;
    left: 0;
    right: 0;
    top: 0;
    height: 12px;
    background: var(--band-dark);
  }
</style>
</head>
<body>
  <main class="letterhead">
    <header class="brand-name">Virtal</header>

    <address class="contact">
      <div>rua das palmeiras 240 2º andar vila nova</div>
      <div>04532 010 são paulo sp brasil</div>
      <div class="phone">+55 11 4820 5517</div>
      <div>www.virtalsolucoesambientais.com.br</div>
    </address>

    <div class="footer-band"></div>
  </main>
</body>
</html>
```